Boat wrap for boat graphics company (Ironic, I know)

We are a boat graphics company, but have a very hard time designing something for ourselves. I would like to refresh our boat wrap. The logo, FB & Insta logos stay as they are. The original (attached) is a simple background from Pixorra.com (#48391206), which I have stretched to give the effect I was looking for. I'm not looking for one of these super colorful / shocking design. Just want something like what I have now, but new. Something flowing, that shows movement (movement, but not necessarily speed). Dark shades of blue are a must, so logo can pop.

Target Market(s)

Boat owners

Industry/Entity Type

Boat / Yacht

Colors
0054AA
0677BA
7BADD7
CADEEF
E8F1F8

Requirements
Must have
• Color Blue
Nice to have
• Not against a marlin texture background, as long as it doesnt interfere with the logo. The Tidal Hull Works boats usually look very cool. These are designed by Twenk
Should not have
• Too many colors

```html
<!DOCTYPE html>
<html lang="en">
<head>
<meta charset="utf-8">
<title>HullWrapsBay.com – Boat Wrap Side Panels</title>
<link rel="stylesheet" href="https://fonts.googleapis.com/css2?family=Federo&display=swap">
<style>
  :root {
    --paper: #ffffff;
    --frame: #1a1a1a;
    --ink-black: #03070f;
    --navy: #022a5c;
    --blue-deep: #0054aa;
    --blue-mid: #0677ba;
    --blue-light: #7badd7;
    --text-white: #ffffff;
    --social-square: #3b5a9a;
  }
  html, body {
    margin: 0;
    padding: 0;
    overflow: hidden;
  }
  .canvas {
    position: relative;
    width: 1200px;
    height: 581px;
    background: var(--paper);
    box-sizing: border-box;
    border: 1px solid var(--frame);
    overflow: hidden;
  }
  .wrap-panel {
    position: absolute;
    left: 67px;
    width: 1065px;
    height: 142px;
    box-sizing: border-box;
    border: 1px solid var(--frame);
    overflow: hidden;
  }
  .wrap-panel--starboard { top: 133px; }
  .wrap-panel--port { top: 313px; }
  .wrap-panel__backdrop {
    position: absolute;
    inset: 0;
  }
  .wrap-panel--starboard .wrap-panel__backdrop {
    background: linear-gradient(155deg,
      var(--blue-deep) 0%, var(--ink-black) 22%, var(--blue-deep) 34%,
      var(--blue-light) 44%, var(--blue-deep) 54%, var(--navy) 66%,
      var(--blue-mid) 76%, var(--ink-black) 90%, var(--navy) 100%);
  }
  .wrap-panel--port .wrap-panel__backdrop {
    background: linear-gradient(25deg,
      var(--navy) 0%, var(--ink-black) 12%, var(--blue-deep) 26%,
      var(--navy) 38%, var(--blue-light) 50%, var(--blue-deep) 62%,
      var(--blue-mid) 76%, var(--ink-black) 88%, var(--blue-deep) 100%);
  }
  .brand-name {
    position: absolute;
    margin: 0;
    font-family: "Federo", sans-serif;
    font-weight: 400;
    font-size: 50px;
    line-height: 1;
    color: var(--text-white);
    white-space: nowrap;
  }
  .wrap-panel--starboard .brand-name { left: 380px; top: 33px; }
  .wrap-panel--port .brand-name { left: 199px; top: 33px; }
  .social-tag {
    position: absolute;
    display: flex;
    align-items: center;
    gap: 6px;
    font-family: "Federo", sans-serif;
    font-weight: 400;
    font-size: 14px;
    color: var(--text-white);
  }
  .social-tag__square {
    width: 28px;
    height: 28px;
    background: var(--social-square);
    border-radius: 3px;
  }
  .wrap-panel--starboard .social-tag { left: 947px; top: 39px; }
  .wrap-panel--port .social-tag { left: 89px; top: 40px; }
</style>
</head>
<body>
  <div class="canvas">
    <section class="wrap-panel wrap-panel--starboard" aria-label="Starboard side wrap">
      <div class="wrap-panel__backdrop" role="img" aria-label="Flowing diagonal streaks in dark blue, light blue and black"></div>
      <p class="brand-name">HullWrapsBay.com</p>
      <div class="social-tag"><span class="social-tag__square"></span><span>Friendloop</span></div>
    </section>
    <section class="wrap-panel wrap-panel--port" aria-label="Port side wrap">
      <div class="wrap-panel__backdrop" role="img" aria-label="Flowing diagonal streaks in dark blue, light blue and black"></div>
      <div class="social-tag"><span class="social-tag__square"></span><span>Friendloop</span></div>
      <p class="brand-name">HullWrapsBay.com</p>
    </section>
  </div>
</body>
</html>
```